Quillora homepage (design only)

We need a high-impact design (alone) for the homepage for a new service to be launched shortly.

Quillora.com will allow consumers to generate a free 'financial personality' report which will help people protect themselves from being mis-sold inappropriate products and services by the financial services industry.

We have upload the Quillora logo and associated artwork. You have totally free reign to use these as you see fit, including using different colours to the lime green we've used.

We ONLY want a design and would prefer it in Illustrator CS5 or lower format rather than Photoshop bitmap. We will write any necessary code or CSS for the final page.

We intend the end site to utilise html5 type animation and effects extensively so if you are picturing an animation, please ensure you explain it with your submission.

The homepage will have five main elements:

1. Navigation:
- Why Quillora
- Security
- Sample report
- Do the test

2. Main section - Quillora : Know Your Financial Personality (you can add ipsum lorum 'explanatory text' if you see fit). This section should refer to the services output, a report which shows five financial characteristics:
- Personality type
- Investment approach
- Knowledge
- Decision biases
- % of UK population like you

3. 'See how you compare against the UK'. An important output of the report is the fact it is linked to extensive UK research. When a user has completed the test, Quillora show him or her via an info graphic, whist percentage of the UK population shares their attributes. Accompnaying tex reads: " If you've ever wondered how you compare to others when it comes to your attitudes on money related matters, quillora will show you". There is an attached file called 'infographic' that illustrates what the end infogrpahic might look like. You can choose to refer to this or elements of this in this section if you choose.

4. 'Cut out the stuff not relevant to you' Accompanying text could be: "Whether it’s language, unnecessarily complex products or stuff that may be too plain risky for you, your Quillora report will help filter out all of the stuff that’s less relevant to you leaving you with choices you understand and decisions that are easier to make." we imagine this section leading to a page that will explain the complexity of products and services before a Quillora report and the small number of relevant services after a quillora report. This section should illustrate that before and after concept.

5. 'Take the test' This section is critical, its the 'call to action' element of the page that links straight to the test. It should illustrate that the test is very short, and very easy.. only two very interactive steps before you get results:
1. Click on the graphics that best describe you.
2. Drag some questions into Quillora 'answer buckets'
3. Done! See the results.
4. Give your free profile to any online service (we make it simple)

The emphasis here is on illustration, typography, colour and impact. We want the site to feel consumer and accessible, not too stuffy and financial, at the same time not too childlike. We are not in favour of typical 'financial' library pics, we'd prefer illustration. Please use your own creativity

Target Market(s)

Adults typically aged 30+ with majority in 40's - 60's. People considering investing or taking any kind of financial advice,

Industry/Entity Type

Financial

Font styles to use
Sans Serif

Requirements
Must have
• The design must include the attached quillora logo albeit the colours used can be entirely at your discretion.
Nice to have
• Site designs we like include:
http://www.ferndashy.com

Should not have
• Design should not contain 'bamboo' clip art. If any quillora type artwork is needed, if should be a derivative of the attached 'bamboo stalk' file. Ideally no stock photography. Illustration and typography should dominate.

Should not use serif fonts

```html
<!DOCTYPE html>
<html lang="en">
<head>
<meta charset="utf-8">
<title>Quillora : Know Your Financial Personality</title>
<link rel="stylesheet" href="https://fonts.googleapis.com/css2?family=Arimo:wght@400;700&display=swap">
<style>
:root{
  --lime:#7cc242;
  --lime-dark:#5e9e2b;
  --ink:#1b1b1b;
  --charcoal:#262626;
  --black:#111111;
  --paper:#f2f2f2;
  --white:#ffffff;
  --grey-text:#c9c9c9;
  --body-text:#222222;
  --orange:#f07c30;
  --bubble-orange:#e8821a;
  --bubble-brown:#6b3a1e;
  --bubble-red:#c9301f;
}
*{box-sizing:border-box;margin:0;padding:0}
html,body{width:1200px;height:3523px;overflow:hidden}
body{position:relative;background:var(--paper);font-family:"Arimo",Arial,sans-serif;color:var(--body-text)}
.abs{position:absolute}

/* top bar */
.top-bar{left:0;top:0;width:1200px;height:28px;background:var(--black);color:#bbb;font-size:12px;line-height:28px;padding-left:156px}

/* header */
.site-header{left:0;top:28px;width:1200px;height:125px;background:#f7f7f7}
.brand{left:146px;top:38px;display:flex;align-items:center;gap:12px}
.brand-dot{width:46px;height:46px;border-radius:50%;background:var(--lime)}
.brand-name{font-size:40px;font-weight:700;color:#333;letter-spacing:-.5px}
.main-nav{left:587px;top:42px;display:flex;gap:10px}
.main-nav a{display:block;font-size:13px;color:#333;text-decoration:none;text-transform:uppercase;padding:0 14px;line-height:42px}
.main-nav a.is-active{background:var(--lime);color:var(--white)}

/* hero */
.hero{left:0;top:153px;width:1200px;height:474px;background:radial-gradient(circle at 50% 45%,#dadada,#c4c4c4)}
.hero-title{left:207px;top:336px;background:#222;border:3px solid var(--lime);color:var(--lime);font-size:34px;font-weight:700;padding:4px 10px;line-height:40px}
.hero-text{left:207px;top:404px;color:#111;font-size:16px;line-height:23px}
.hero-figure{left:812px;top:176px;width:150px;height:446px;border-radius:14px;background:linear-gradient(160deg,#a9bfd6,#6f7f91)}
.slider-arrows{left:291px;top:589px;display:flex}
.slider-arrows span{width:37px;height:38px;display:flex;align-items:center;justify-content:center}
.slider-arrows .prev{background:var(--lime)}
.slider-arrows .next{background:var(--black)}

/* intro band */
.intro{left:0;top:627px;width:1200px;height:270px;background:var(--lime);color:var(--white)}
.intro h2{position:absolute;left:171px;top:38px;font-size:30px;font-weight:700}
.intro p{position:absolute;left:171px;top:96px;width:858px;font-size:12px;line-height:24px}

/* features icons */
.features{left:0;top:897px;width:1200px;height:246px;background:var(--paper)}
.feature{position:absolute;top:66px;width:150px;text-align:center}
.feature-icon{width:75px;height:75px;margin:0 auto;background:var(--lime);border-bottom:5px solid var(--lime-dark);display:flex;align-items:center;justify-content:center;box-shadow:0 8px 8px -4px rgba(0,0,0,.35)}
.feature-label{margin-top:30px;font-size:13px;color:#444;text-transform:uppercase}

/* dark section */
.band-title{left:0;top:1143px;width:1200px;height:59px;background:var(--black);color:var(--white);font-size:27px;font-weight:700;text-align:center;line-height:59px}
.benefits{left:0;top:1202px;width:1200px;height:512px;background:var(--charcoal)}
.benefits .rule-v{left:610px;top:30px;width:1px;height:452px;background:#3d3d3d}
.benefits .rule-h{left:195px;top:235px;width:923px;height:1px;background:#3d3d3d}
.benefit{position:absolute;width:295px}
.benefit svg{position:absolute;left:-62px;top:-18px}
.benefit h3{color:var(--white);font-size:20px;font-weight:700;margin-bottom:10px}
.benefit p{color:var(--grey-text);font-size:13px;line-height:19px}

/* compare section */
.section-title{left:0;width:1200px;text-align:center;font-size:29px;font-weight:700;color:var(--ink)}
.infographic{left:0;top:1843px}
.infographic text{font-family:"Arimo",Arial,sans-serif}
.mascot{left:188px;top:2219px;width:117px;height:199px;border-radius:14px;background:linear-gradient(160deg,#8a8f96,#3a3d42)}
.compare-text{left:324px;top:2313px;width:720px;font-size:12px;line-height:22px}
.divider{left:148px;top:2477px;width:909px;height:2px;background:#cfcfcf}

/* filter items */
.story h3{position:absolute;font-size:21px;font-weight:700;color:var(--ink)}
.story p{position:absolute;font-size:11.5px;line-height:22px}
.illustration{position:absolute;border-radius:14px}
.illustration-orange{left:170px;top:2583px;width:92px;height:246px;background:linear-gradient(var(--bubble-orange),#d9b48a)}
.illustration-brown{left:880px;top:2829px;width:138px;height:247px;background:linear-gradient(var(--bubble-brown),#8d8f94)}
.illustration-red{left:155px;top:3064px;width:125px;height:256px;background:linear-gradient(var(--bubble-red),#dccbb6)}

/* footer */
.site-footer{left:0;top:3327px;width:1200px;height:136px;background:var(--lime)}
.footer-nav{position:absolute;left:0;top:96px;width:1200px;display:flex;justify-content:center;gap:47px}
.footer-nav a{color:var(--white);font-size:12px;font-weight:700;text-decoration:none;text-transform:uppercase}
.base-bar{left:0;top:3463px;width:1200px;height:60px;background:var(--black)}
</style>
</head>
<body>

<div class="abs top-bar">Phone: 415.555.0182</div>

<header class="abs site-header">
  <div class="abs brand"><span class="brand-dot"></span><span class="brand-name">Quillora</span></div>
  <nav class="abs main-nav">
    <a href="#" class="is-active">Why Quillora</a>
    <a href="#">Security</a>
    <a href="#">Sample report</a>
    <a href="#">Do the test</a>
  </nav>
</header>

<section class="abs hero" role="img" aria-label="Softly patterned grey backdrop"></section>
<h1 class="abs hero-title">LOREM IPSUM DOLOR</h1>
<p class="abs hero-text">Lorem ipsum dolor sit amet, consectetur adipisicing elit,<br>sed do eiusmod tempor incididunt ut labore et dolore magna aliqua.</p>
<div class="abs hero-figure" role="img" aria-label="Illustrated cheerful man in shirt and tie holding a tablet"></div>
<div class="abs slider-arrows">
  <span class="prev"><svg width="12" height="16" viewBox="0 0 12 16"><path d="M9 2L3 8l6 6" fill="none" stroke="#fff" stroke-width="2"/></svg></span>
  <span class="next"><svg width="12" height="16" viewBox="0 0 12 16"><path d="M3 2l6 6-6 6" fill="none" stroke="#fff" stroke-width="2"/></svg></span>
</div>

<section class="abs intro">
  <h2>LOREM IPSUM DOLOR</h2>
  <p>Lorem ipsum dolor sit amet, consectetur adipisicing elit, sed do eiusmod tempor incididunt ut labore et dolore magna aliqua. Ut enim ad minim veniam, quis nostrud exercitation ullamco laboris nisi ut aliquip ex ea commodo consequat. Duis aute irure dolor in reprehenderit in voluptate velit esse cillum dolore eu fugiat nulla pariatur. Excepteur sint occaecat cupidatat non proident, sunt in culpa qui officia deserunt mollit anim id est laborum. Lorem ipsum dolor sit amet, consectetur adipisicing elit, sed do eiusmod tempor incididunt ut labore et dolore magna aliqua. Ut enim ad minim veniam, quis nostrud exercitation ullamco laboris nisi ut aliquip ex ea commodo consequat. Duis aute irure dolor in reprehenderit in voluptate velit esse cillum dolore eu fugiat nulla pariatur.</p>
</section>

<section class="abs features">
  <div class="feature" style="left:221px">
    <div class="feature-icon"><svg width="38" height="34" viewBox="0 0 38 34"><rect x="2" y="2" width="34" height="22" fill="none" stroke="#fff" stroke-width="3"/><path d="M12 32h14M19 24v8" stroke="#fff" stroke-width="3"/></svg></div>
    <div class="feature-label">Lorem lipsum</div>
  </div>
  <div class="feature" style="left:426px">
    <div class="feature-icon"><svg width="38" height="34" viewBox="0 0 38 34"><path d="M2 12h34l-4 20H6z" fill="#fff"/><path d="M11 12l6-10M27 12l-6-10" stroke="#fff" stroke-width="3"/><path d="M13 17v10M19 17v10M25 17v10" stroke="#7cc242" stroke-width="2"/></svg></div>
    <div class="feature-label">Lorem lipsum</div>
  </div>
  <div class="feature" style="left:628px">
    <div class="feature-icon"><svg width="36" height="34" viewBox="0 0 36 34"><path d="M4 10h6v20H4zM13 4h6v26h-6zM22 14h6v16h-6z" fill="#fff"/><path d="M1 32h34" stroke="#fff" stroke-width="3"/></svg></div>
    <div class="feature-label">Lorem lipsum</div>
  </div>
  <div class="feature" style="left:827px">
    <div class="feature-icon"><svg width="36" height="28" viewBox="0 0 36 28"><path d="M13 4L3 14l10 10M23 4l10 10-10 10" fill="none" stroke="#fff" stroke-width="4"/></svg></div>
    <div class="feature-label">Lorem lipsum</div>
  </div>
</section>

<h2 class="abs band-title">LOREM IPSUM DOLOR SIT AMET</h2>
<section class="abs benefits">
  <div class="abs rule-v"></div>
  <div class="abs rule-h"></div>
  <article class="benefit" style="left:279px;top:95px">
    <svg width="40" height="56" viewBox="0 0 40 56"><rect x="4" y="2" width="28" height="44" rx="3" fill="none" stroke="#7cc242" stroke-width="3"/><rect x="22" y="18" width="16" height="30" rx="2" fill="#262626" stroke="#7cc242" stroke-width="3"/></svg>
    <h3>LOREM IPSUM DOLOR</h3>
    <p>Lorem ipsum dolor sit amet, consectetur adipisicing elit, sed do eiusmod tempor incididunt.</p>
  </article>
  <article class="benefit" style="left:758px;top:95px">
    <svg width="56" height="56" viewBox="0 0 56 56" style="left:-80px"><circle cx="28" cy="28" r="24" fill="none" stroke="#7cc242" stroke-width="3"/><ellipse cx="28" cy="28" rx="11" ry="24" fill="none" stroke="#7cc242" stroke-width="3"/><path d="M4 28h48M9 15h38M9 41h38" stroke="#7cc242" stroke-width="3"/></svg>
    <h3>LOREM IPSUM DOLOR</h3>
    <p>Lorem ipsum dolor sit amet, consectetur adipisicing elit, sed do eiusmod tempor incididunt.</p>
  </article>
  <article class="benefit" style="left:279px;top:295px">
    <svg width="60" height="56" viewBox="0 0 60 56" style="left:-72px;top:-30px"><circle cx="22" cy="34" r="12" fill="none" stroke="#7cc242" stroke-width="8" stroke-dasharray="5 4"/><circle cx="22" cy="34" r="7" fill="#7cc242"/><circle cx="45" cy="16" r="8" fill="none" stroke="#7cc242" stroke-width="6" stroke-dasharray="4 3"/><circle cx="45" cy="16" r="4" fill="#7cc242"/></svg>
    <h3>LOREM IPSUM DOLOR</h3>
    <p>Lorem ipsum dolor sit amet, consectetur adipisicing elit, sed do eiusmod tempor incididunt.</p>
  </article>
  <article class="benefit" style="left:758px;top:295px">
    <svg width="60" height="56" viewBox="0 0 60 56" style="left:-76px;top:-28px"><path d="M6 50h10V36H6zM20 50h10V28H20zM34 50h10V20H34z" fill="#7cc242"/><path d="M6 30L24 14l10 8L52 4" fill="none" stroke="#7cc242" stroke-width="4"/><path d="M42 3h12v12z" fill="#7cc242"/></svg>
    <h3>LOREM IPSUM DOLOR</h3>
    <p>Lorem ipsum dolor sit amet, consectetur adipisicing elit, sed do eiusmod tempor incididunt.</p>
  </article>
</section>

<h2 class="abs section-title" style="top:1768px">LOREM IPSUM DOLOR SIT AMET</h2>

<svg class="abs infographic" width="1200" height="410" viewBox="0 1843 1200 410" role="img" aria-label="Infographic path comparing gender, age, financial knowledge and risk aptitude with the share of people alike">
  <path d="M200 1896V2040q0 15 15 15H470q15 0 15 15V2200q0 15 15 15H955q15 0 15-15V2138" fill="none" stroke="#777" stroke-width="7"/>
  <circle cx="200" cy="1872" r="24" fill="none" stroke="#777" stroke-width="7"/>
  <circle cx="970" cy="2112" r="25" fill="none" stroke="#777" stroke-width="7"/>
  <text x="232" y="1880" font-size="14" fill="#888">Mike</text>
  <g fill="#f07c30"><circle cx="240" cy="2055" r="4"/><circle cx="305" cy="2055" r="4"/><circle cx="560" cy="2215" r="4"/><circle cx="750" cy="2215" r="4"/></g>
  <text x="216" y="2080" font-size="14" fill="#888">Gender</text>
  <text x="298" y="2080" font-size="14" fill="#888">Age</text>
  <circle cx="240" cy="1980" r="13" fill="#f07c30"/><text x="240" y="1984" font-size="9" fill="#fff" text-anchor="middle">40%</text>
  <circle cx="301" cy="1980" r="13" fill="#f07c30"/><text x="301" y="1984" font-size="9" fill="#fff" text-anchor="middle">60%</text>
  <g fill="#4a9bd6"><circle cx="240" cy="2003" r="5"/><rect x="235" y="2010" width="10" height="20"/></g>
  <g fill="#e889c4"><circle cx="270" cy="2003" r="5"/><path d="M270 2009l7 14h-14z"/><rect x="266" y="2022" width="8" height="8"/></g>
  <g fill="#666" font-size="9">
    <rect x="305" y="1944" width="14" height="8"/><text x="328" y="1952">30% - 18%</text>
    <rect x="305" y="1964" width="14" height="8"/><text x="328" y="1972" font-weight="700" fill="#222">40%</text>
    <rect x="305" y="1984" width="14" height="8"/><text x="328" y="1992">50% - 28%</text>
    <rect x="305" y="2004" width="14" height="8"/><text x="328" y="2012">60% - 15%</text>
  </g>
  <g fill="#bdbdbd"><circle cx="560" cy="1967" r="20"/><circle cx="560" cy="2095" r="22"/><circle cx="560" cy="2160" r="22"/></g>
  <circle cx="560" cy="2030" r="26" fill="#f07c30"/>
  <g font-size="11" fill="#fff" text-anchor="middle"><text x="560" y="2034">28%</text><text x="560" y="2099">27%</text></g>
  <g fill="#bdbdbd"><circle cx="751" cy="1918" r="19"/><circle cx="751" cy="2043" r="22"/><circle cx="751" cy="2108" r="22"/><circle cx="751" cy="2179" r="20"/></g>
  <circle cx="751" cy="1975" r="20" fill="#f07c30"/><text x="751" y="1979" font-size="11" fill="#fff" text-anchor="middle">16%</text>
  <text x="512" y="2234" font-size="14" fill="#888">Financial Knowledge</text>
  <text x="707" y="2234" font-size="14" fill="#888">Risk aptitude</text>
  <text x="940" y="1996" font-size="14" fill="#666">% like me</text>
  <g fill="#4a9bd6">
    <circle cx="952" cy="2016" r="4"/><circle cx="964" cy="2016" r="4"/><circle cx="976" cy="2016" r="4"/><circle cx="988" cy="2016" r="4"/><circle cx="1000" cy="2016" r="4"/>
  </g>
  <g fill="#9aa3aa">
    <circle cx="952" cy="2034" r="4"/><circle cx="964" cy="2034" r="4"/><circle cx="976" cy="2034" r="4"/><circle cx="988" cy="2034" r="4"/><circle cx="1000" cy="2034" r="4"/>
    <circle cx="952" cy="2052" r="4"/><circle cx="964" cy="2052" r="4"/><circle cx="976" cy="2052" r="4"/><circle cx="988" cy="2052" r="4"/><circle cx="1000" cy="2052" r="4"/>
    <circle cx="952" cy="2070" r="4"/><circle cx="964" cy="2070" r="4"/><circle cx="976" cy="2070" r="4"/><circle cx="988" cy="2070" r="4"/><circle cx="1000" cy="2070" r="4"/>
  </g>
</svg>

<div class="abs mascot" role="img" aria-label="Illustrated businessman working on a laptop"></div>
<p class="abs compare-text">Lorem ipsum dolor sit amet, consectetur adipisicing elit, sed do eiusmod tempor incididunt ut labore et dolore magna aliqua. Ut enim ad minim veniam, quis nostrud exercitation ullamco laboris nisi ut aliquip ex ea commodo consequat. Duis aute irure dolor in reprehenderit in voluptate velit esse cillum dolore eu fugiat nulla pariatur. Excepteur sint occaecat cupidatat non proident, sunt in culpa qui officia deserunt mollit anim id est laborum.</p>

<div class="abs divider"></div>

<h2 class="abs section-title" style="top:2513px">LOREM IPSUM DOLOR SIT AMET</h2>

<section class="story">
  <div class="illustration illustration-orange" role="img" aria-label="Orange speech bubble above a woman seated in a round chair"></div>
  <h3 style="left:305px;top:2688px">LOREM IPSUM DOLOR</h3>
  <p style="left:305px;top:2725px;width:590px">Lorem ipsum dolor sit amet, consectetur adipisicing elit, sed do eiusmod tempor incididunt ut labore et dolore magna aliqua. Ut enim ad minim veniam, quis nostrud exercitation ullamco laboris nisi ut aliquip ex ea commodo consequat. Duis aute irure dolor in reprehenderit in voluptate velit esse cillum dolore eu fugiat nulla pariatur. Excepteur sint occaecat cupidatat non proident, sunt in culpa qui officia deserunt mollit anim id est laborum.</p>

  <h3 style="left:167px;top:2906px">LOREM IPSUM DOLOR</h3>
  <p style="left:167px;top:2942px;width:680px">Lorem ipsum dolor sit amet, consectetur adipisicing elit, sed do eiusmod tempor incididunt ut labore et dolore magna aliqua. Ut enim ad minim veniam, quis nostrud exercitation ullamco laboris nisi ut aliquip ex ea commodo consequat. Duis aute irure dolor in reprehenderit in voluptate velit esse cillum dolore eu fugiat nulla pariatur. Excepteur sint occaecat cupidatat non proident, sunt in culpa qui officia deserunt mollit anim id est laborum.</p>
  <div class="illustration illustration-brown" role="img" aria-label="Brown speech bubble above a man seated in an office chair"></div>

  <div class="illustration illustration-red" role="img" aria-label="Red speech bubble above a woman reclining in a red chair"></div>
  <h3 style="left:326px;top:3148px">LOREM IPSUM DOLOR</h3>
  <p style="left:326px;top:3185px;width:590px">Lorem ipsum dolor sit amet, consectetur adipisicing elit, sed do eiusmod tempor incididunt ut labore et dolore magna aliqua. Ut enim ad minim veniam, quis nostrud exercitation ullamco laboris nisi ut aliquip ex ea commodo consequat. Duis aute irure dolor in reprehenderit in voluptate velit esse cillum dolore eu fugiat nulla pariatur. Excepteur sint occaecat cupidatat non proident, sunt in culpa qui officia deserunt mollit anim id est laborum.</p>
</section>

<footer class="abs site-footer">
  <nav class="footer-nav">
    <a href="#">Why Quillora</a>
    <a href="#">Security</a>
    <a href="#">Sample report</a>
    <a href="#">Do the test</a>
  </nav>
</footer>
<div class="abs base-bar"></div>

</body>
</html>
```